ALL ASPECTS OF PLASTERING INC: TEXTURE,SANDFINISH RENO,POOLS, PATCH WORK ( STATEWIDE SERVICE GOOD RATES) 100% GUARANTEED FULLY INSURED C

Target Market(s)

ANYONE WHO OWNS A HOUSE,BUILDERS

Industry/Entity Type

Work

Contact Information for Business Card

GRITT-WALL PLASTERING SERVICES
BERNARD KOVALEC 0438259164
EMAIL:TARVEK48@QUILLMAIL.COM

Requirements
Must have
• COLOUR BACKGROUND WIV PLASTERING PICTURE EG TROWEL, CEMENT MIXER, SAND
Nice to have
• BOLD PROFESSIONAL LOOKING AND SOUNDING CATCHY SAYING
Should not have
• FLURO COLOURS

```html
<!DOCTYPE html>
<html lang="en">
<head>
<meta charset="utf-8">
<title>Gritt-Wall Plastering Services – Business Card</title>
<link rel="stylesheet" href="https://fonts.googleapis.com/css2?family=Roboto+Condensed:wght@400;700&family=Open+Sans:wght@300;400&display=swap">
<style>
  :root {
    --page-bg: #ffffff;
    --card-bg: #4a4b4d;
    --ink-dark: #1e1f21;
    --ink-muted: #7a7b7e;
  }
  * { box-sizing: border-box; margin: 0; padding: 0; }
  html, body {
    width: 1200px;
    height: 476px;
    overflow: hidden;
    background: var(--page-bg);
  }
  .canvas {
    position: relative;
    width: 1200px;
    height: 476px;
  }
  .card {
    position: absolute;
    top: 66px;
    height: 330px;
    background: var(--card-bg);
    border-radius: 14px;
  }
  .card--front { left: 104px; width: 492px; }
  .card--back  { left: 618px; width: 500px; }

  .brand {
    position: absolute;
    left: 26px;
    top: 28px;
    display: flex;
    align-items: center;
    gap: 10px;
  }
  .brand__mark {
    width: 14px;
    height: 14px;
    background: var(--ink-dark);
  }
  .brand__name {
    font-family: "Roboto Condensed", "Arial Narrow", sans-serif;
    font-weight: 700;
    font-size: 18px;
    letter-spacing: 0.5px;
    color: var(--ink-dark);
  }

  .contact {
    position: absolute;
    right: 26px;
    top: 124px;
    text-align: right;
  }
  .contact__name {
    font-family: "Roboto Condensed", "Arial Narrow", sans-serif;
    font-weight: 700;
    font-size: 23px;
    letter-spacing: 0.5px;
    color: var(--ink-dark);
    margin-bottom: 6px;
  }
  .contact__line {
    font-family: "Open Sans", Arial, sans-serif;
    font-weight: 300;
    font-size: 12px;
    line-height: 16px;
    color: var(--ink-muted);
  }

  .services {
    position: absolute;
    left: 0;
    right: 0;
    top: 104px;
    text-align: center;
    font-family: "Roboto Condensed", "Arial Narrow", sans-serif;
    font-weight: 400;
    font-size: 19px;
    line-height: 33px;
    color: var(--ink-dark);
  }
</style>
</head>
<body>
  <main class="canvas">
    <section class="card card--front">
      <div class="brand">
        <span class="brand__mark"></span>
        <h1 class="brand__name">GRITT-WALL PLASTERING SERVICES</h1>
      </div>
      <div class="contact">
        <p class="contact__name">BERNARD KOVALEC</p>
        <p class="contact__line">Phone: 0438259164</p>
        <p class="contact__line">Email: tarvek48@quillmail.com</p>
      </div>
    </section>

    <section class="card card--back">
      <p class="services">
        ALL ASPECTS OF PLASTERING INC:<br>
        TEXTURE,SANDFINISH RENO,POOLS,<br>
        PATCH WORK ( STATEWIDE SERVICE GOOD RATES)
      </p>
    </section>
  </main>
</body>
</html>
```